Travel Blogger Business Card for roamquill.net

I need a two-sided business card for a travel blogging website. The card should be both professional and fun at the same time. This is for the website www.roamquill.net

I don't necessarily think that the current logo on the website needs to be used on the business card but it can be. I am very flexible with ideas

Target Market(s)

Travel agencies that will be met at a conference.

Industry/Entity Type

Travel

Contact Information for Business Card

Company Name: Roam Quill.net
Name: Bertrand Olesky
Voice: +1-(345)-402-7731
Address: Coral Reach Shore, Grand Cayman, Cayman Islands
Email: ceo@roamquill.net

Colors
0592cd
0355a3
3176b5
33a6d7
85cae6
85acd3

Requirements
Must have
• Website address and name should be bigger than address, phone number, and email.

```html
<!DOCTYPE html>
<html lang="en">
<head>
<meta charset="utf-8">
<title>Roam Quill.net – Business Card</title>
<link rel="stylesheet" href="https://fonts.googleapis.com/css2?family=Montserrat:wght@600;800&family=Patrick+Hand&display=swap">
<style>
  :root {
    --backdrop: #2e2e30;
    --card-black: #1b1b1c;
    --white: #ffffff;
    --orange: #f26522;
    --orange-light: #f47a26;
    --sky-blue: #1aa3d6;
    --deep-teal: #16475a;
    --warm-cream: #ffe6cc;
    --icon-orange: #f7941d;
  }
  * { margin: 0; padding: 0; box-sizing: border-box; }
  html, body {
    width: 1200px;
    height: 852px;
    overflow: hidden;
    background: var(--backdrop);
  }
  .stage { position: relative; width: 1200px; height: 852px; }

  .card {
    position: absolute;
    width: 560px;
    height: 320px;
    border-radius: 20px;
    overflow: hidden;
    box-shadow: 0 10px 30px rgba(0,0,0,0.45);
  }

  /* Back side */
  .card-back {
    left: 90px;
    top: 100px;
    background: var(--card-black);
  }
  .card-back .brand {
    position: absolute;
    left: 52px;
    top: 110px;
    display: flex;
    align-items: center;
    gap: 18px;
  }
  .brand-dot {
    width: 64px;
    height: 64px;
    border-radius: 50%;
    background: var(--white);
    flex: none;
  }
  .brand-name {
    font-family: "Montserrat", sans-serif;
    font-weight: 800;
    font-size: 33px;
    letter-spacing: 0.5px;
    color: var(--white);
    line-height: 1;
  }
  .tagline {
    margin-top: 8px;
    width: 370px;
    font-family: "Patrick Hand", cursive;
    font-size: 13px;
    line-height: 1.25;
    color: var(--white);
  }

  /* Front side */
  .card-front {
    left: 550px;
    top: 450px;
    background: linear-gradient(90deg, var(--orange) 0%, var(--orange-light) 100%);
  }
  .card-front .wave-area {
    position: absolute;
    left: 0;
    bottom: 0;
    width: 560px;
    height: 170px;
  }
  .card-front .brand {
    position: absolute;
    left: 40px;
    top: 70px;
    display: flex;
    align-items: center;
    gap: 14px;
  }
  .card-front .brand-dot { width: 50px; height: 50px; }
  .card-front .brand-name { font-size: 31px; }
  .address {
    margin-top: 6px;
    font-family: "Patrick Hand", cursive;
    font-size: 16px;
    color: var(--warm-cream);
    line-height: 1;
  }
  .contact {
    position: absolute;
    left: 38px;
    top: 228px;
    color: var(--white);
    font-family: "Montserrat", sans-serif;
  }
  .person-name {
    font-weight: 800;
    font-size: 19px;
    margin-bottom: 6px;
  }
  .contact-line {
    display: flex;
    align-items: center;
    gap: 8px;
    font-weight: 600;
    font-size: 12px;
    line-height: 1.6;
  }
  .contact-icon { width: 11px; height: 11px; flex: none; }
</style>
</head>
<body>
<main class="stage">

  <section class="card card-back" aria-label="Card back">
    <div class="brand">
      <span class="brand-dot"></span>
      <div>
        <div class="brand-name">ROAM QUILL.NET</div>
        <p class="tagline">We are Canadians who live in the Caribbean and travel full-time. The more we travel the more we realize how little we have seen.</p>
      </div>
    </div>
  </section>

  <section class="card card-front" aria-label="Card front">
    <svg class="wave-area" viewBox="0 0 560 170" preserveAspectRatio="none" role="img" aria-label="Ocean wave artwork in blue and teal">
      <defs>
        <linearGradient id="wave-fill" x1="0" y1="0" x2="0" y2="1">
          <stop offset="0" stop-color="var(--sky-blue)"/>
          <stop offset="0.35" stop-color="var(--deep-teal)"/>
        </linearGradient>
      </defs>
      <path d="M0,60 C200,20 380,60 560,0 L560,170 L0,170 Z" fill="url(#wave-fill)"/>
    </svg>

    <div class="brand">
      <span class="brand-dot"></span>
      <div>
        <div class="brand-name">ROAM QUILL.NET</div>
        <p class="address">Coral Reach Shore, Grand Cayman, Cayman Islands</p>
      </div>
    </div>

    <div class="contact">
      <p class="person-name">Bertrand Olesky</p>
      <p class="contact-line">
        <svg class="contact-icon" viewBox="0 0 24 24" aria-hidden="true"><path fill="var(--icon-orange)" d="M6.6 10.8a15.1 15.1 0 0 0 6.6 6.6l2.2-2.2c.3-.3.7-.4 1-.2 1.1.4 2.3.6 3.6.6.6 0 1 .4 1 1V20c0 .6-.4 1-1 1A17 17 0 0 1 3 4c0-.6.4-1 1-1h3.5c.6 0 1 .4 1 1 0 1.3.2 2.5.6 3.6.1.3 0 .7-.2 1z"/></svg>
        +1-(345)-402-7731
      </p>
      <p class="contact-line">
        <svg class="contact-icon" viewBox="0 0 24 24" aria-hidden="true"><rect x="2" y="5" width="20" height="14" rx="1.5" fill="var(--icon-orange)"/><path d="M3 6l9 7 9-7" fill="none" stroke="var(--deep-teal)" stroke-width="2"/></svg>
        ceo@roamquill.net
      </p>
    </div>
  </section>

</main>
</body>
</html>
```